Smoked and Dried Fish Business Cards

We need a business card design for a new company called The Copperwake Limited. We import smoked and dried fish from Ghana and distribute worldwide. We would like to see designs that use colours red yellow and green. The final design should communicate healthy and saftey food environment.

Industry/Entity Type

Business

Contact Information for Business Card

The Copperwake Limited.
87 Brindle Row. Hollin Vale.
London.
SE14 3QJ.
TEL: 01632 960417. Mobile. 07700 900318 /07700900562
Website: www.copperwakeltd.com email: sales@copperwakeltd.com

```html
<!DOCTYPE html>
<html lang="en">
<head>
<meta charset="utf-8">
<title>The Copperwake Limited – Business Card</title>
<link href="https://fonts.googleapis.com/css2?family=Marcellus&display=swap" rel="stylesheet">
<style>
  :root {
    --page-bg: #e4e4e2;
    --card-green: #3e7b3b;
    --card-olive: #8f9c3e;
    --ink-yellow: #f2ec7e;
    --card-shadow: rgba(0, 0, 0, 0.28);
  }
  * { box-sizing: border-box; margin: 0; padding: 0; }
  html, body {
    width: 1200px;
    height: 900px;
    overflow: hidden;
    background: var(--page-bg);
  }
  .canvas {
    position: relative;
    width: 1200px;
    height: 900px;
  }
  .business-card {
    position: absolute;
    left: 100px;
    top: 155px;
    width: 1000px;
    height: 590px;
    background: var(--card-green);
    box-shadow: 0 18px 40px var(--card-shadow);
    overflow: hidden;
    font-family: "Marcellus", Georgia, serif;
    color: var(--ink-yellow);
  }
  .fish-motif {
    position: absolute;
    left: 150px;
    top: 110px;
    width: 700px;
    height: 380px;
  }
  .company-name {
    position: absolute;
    left: 150px;
    top: 218px;
    font-size: 60px;
    font-weight: 400;
    letter-spacing: 0.5px;
    white-space: nowrap;
  }
  .company-address {
    position: absolute;
    left: 290px;
    top: 305px;
    font-size: 23px;
    white-space: nowrap;
  }
  .contact {
    position: absolute;
    font-size: 23px;
    white-space: nowrap;
  }
  .contact__rule {
    display: block;
    height: 2px;
    background: var(--ink-yellow);
    margin: 4px 0;
  }
  .contact__icon {
    display: block;
    width: 28px;
    height: 28px;
  }
  .contact--mobile-main { left: 80px; top: 36px; width: 210px; }
  .contact--mobile-main .contact__icon { margin-left: 30px; }
  .contact--landline { left: 400px; top: 50px; width: 210px; text-align: center; }
  .contact--landline .contact__icon { margin: 0 auto; }
  .contact--mobile-alt { left: 740px; top: 100px; width: 210px; }
  .contact--mobile-alt .contact__icon { margin-left: 140px; }
  .contact--email { left: 50px; top: 395px; width: 300px; }
  .contact--email .contact__icon { margin-left: 150px; width: 34px; }
  .contact--web { left: 560px; top: 445px; width: 330px; }
  .contact--web .contact__icon { margin-left: 170px; }
</style>
</head>
<body>
<main class="canvas">
  <section class="business-card">
    <svg class="fish-motif" role="img" aria-label="Fish illustration in olive with soft ripple rings" viewBox="0 0 700 380">
      <ellipse cx="350" cy="190" rx="345" ry="185" fill="var(--card-olive)" opacity="0.85"/>
    </svg>

    <div class="contact contact--mobile-main">
      <span class="contact__text">07700 900318</span>
      <span class="contact__rule"></span>
      <svg class="contact__icon" viewBox="0 0 28 28" aria-hidden="true">
        <rect x="9" y="3" width="11" height="21" rx="2" fill="none" stroke="var(--ink-yellow)" stroke-width="2"/>
        <line x1="12" y1="20" x2="17" y2="20" stroke="var(--ink-yellow)" stroke-width="2"/>
      </svg>
    </div>

    <div class="contact contact--landline">
      <span class="contact__text">01632 960417</span>
      <span class="contact__rule"></span>
      <svg class="contact__icon" viewBox="0 0 28 28" aria-hidden="true">
        <rect x="3" y="3" width="22" height="22" rx="4" fill="var(--ink-yellow)"/>
        <path d="M10 8c-2 2-1 7 3 11s7 4 8 2l-3-3-2 1c-2-1-4-3-5-5l1-2z" fill="var(--card-green)"/>
      </svg>
    </div>

    <div class="contact contact--mobile-alt">
      <span class="contact__text">07700900562</span>
      <span class="contact__rule"></span>
      <svg class="contact__icon" viewBox="0 0 28 28" aria-hidden="true">
        <rect x="4" y="9" width="20" height="11" rx="2" fill="none" stroke="var(--ink-yellow)" stroke-width="2" transform="rotate(-25 14 14)"/>
      </svg>
    </div>

    <h1 class="company-name">The Copperwake Limited.</h1>
    <p class="company-address">87 Brindle Row, Hollin Vale, London, SE14 3QJ.</p>

    <div class="contact contact--email">
      <svg class="contact__icon" viewBox="0 0 34 28" aria-hidden="true">
        <rect x="2" y="5" width="30" height="19" fill="none" stroke="var(--ink-yellow)" stroke-width="2"/>
        <path d="M2 5l15 11 15-11" fill="none" stroke="var(--ink-yellow)" stroke-width="2"/>
      </svg>
      <span class="contact__rule"></span>
      <span class="contact__text">sales@copperwakeltd.com</span>
    </div>

    <div class="contact contact--web">
      <svg class="contact__icon" viewBox="0 0 28 28" aria-hidden="true">
        <circle cx="14" cy="14" r="11" fill="none" stroke="var(--ink-yellow)" stroke-width="2"/>
        <ellipse cx="14" cy="14" rx="5" ry="11" fill="none" stroke="var(--ink-yellow)" stroke-width="1.5"/>
        <line x1="3" y1="14" x2="25" y2="14" stroke="var(--ink-yellow)" stroke-width="1.5"/>
      </svg>
      <span class="contact__rule"></span>
      <span class="contact__text">www.copperwakeltd.com</span>
    </div>
  </section>
</main>
</body>
</html>
```